Marlow Crest Group (Real Estate and Investment)

A high end, clean design.
We are a real estate company with sales, asset management and investment divisions. We want to use a black and white scheme which is really high end feel. The back of the card can just be the logo (black background with the white writing) as we will probably emboss this when we print)

Target Market(s)

High level investors, high end houses for sale

Industry/Entity Type

Business

Contact Information for Business Card

Name, position, phone number and email address
Glen Varley, Managing Director, 0437259064 and glen@marlowcrest-example.com.au

Requirements
Must have
• Back of the card to be the black background with the white writing (as per the attached images). Would like the capacity to emboss the writing and logo

```html
<!DOCTYPE html>
<html lang="en">
<head>
<meta charset="utf-8">
<title>Marlow Crest Group – Business Card</title>
<link href="https://fonts.googleapis.com/css2?family=Poppins:wght@300;400;500;600&display=swap" rel="stylesheet">
<style>
  :root {
    --backdrop: #e6e6e6;
    --card-black: #121212;
    --card-white: #ffffff;
    --ink-white: #f4f4f4;
    --ink-grey: #5a5a5a;
    --rule-grey: #8a8a8a;
    --emboss-ring: #2e2e2e;
  }
  * { margin: 0; padding: 0; box-sizing: border-box; }
  html, body {
    width: 1200px;
    height: 1000px;
    overflow: hidden;
    background: var(--backdrop);
    font-family: "Poppins", sans-serif;
  }
  .stage {
    position: relative;
    width: 1200px;
    height: 1000px;
  }
  .card {
    position: absolute;
    left: 290px;
    width: 620px;
    height: 378px;
    box-shadow: 0 6px 18px rgba(0,0,0,0.18);
  }
  .card--back {
    top: 80px;
    background: var(--card-black);
    display: flex;
    flex-direction: column;
    align-items: center;
    justify-content: center;
    gap: 22px;
  }
  .brand-mark {
    width: 64px;
    height: 64px;
  }
  .brand-name {
    color: var(--ink-white);
    font-weight: 400;
    font-size: 26px;
    letter-spacing: 0.04em;
    text-transform: uppercase;
  }
  .card--front {
    top: 520px;
    background: var(--card-white);
    display: flex;
    flex-direction: column;
    align-items: center;
    justify-content: center;
    color: var(--ink-grey);
    text-align: center;
  }
  .rule {
    width: 30px;
    height: 1px;
    background: var(--rule-grey);
  }
  .rule--top { margin-bottom: 36px; }
  .rule--bottom { margin-top: 36px; }
  .person-name {
    font-size: 26px;
    font-weight: 400;
    line-height: 1.2;
  }
  .person-name .surname { font-weight: 500; }
  .person-title {
    font-size: 14px;
    font-weight: 400;
    margin-top: 2px;
  }
  .contact-line {
    font-size: 15px;
    font-weight: 300;
    margin-top: 8px;
  }
</style>
</head>
<body>
  <main class="stage">
    <section class="card card--back" aria-label="Card back">
      <svg class="brand-mark" viewBox="0 0 64 64" aria-hidden="true">
        <circle cx="32" cy="32" r="29" fill="none" stroke="var(--emboss-ring)" stroke-width="2"/>
      </svg>
      <h1 class="brand-name">Marlow Crest Group</h1>
    </section>

    <section class="card card--front" aria-label="Card front">
      <div class="rule rule--top"></div>
      <h2 class="person-name">Glen <span class="surname">Varley</span></h2>
      <p class="person-title">Managing Director</p>
      <p class="contact-line">P: 0437259064 | E: glen@marlowcrest-example.com.au</p>
      <div class="rule rule--bottom"></div>
    </section>
  </main>
</body>
</html>
```